【テキスト】
ーーーーーーーーーーーーー
(メインタイトル)
黄金羅針盤アカデミー
実践攻略
前編
(サブタイトル)
相続市場を狙え!!
利回り20%&転売益2000万!
ーーーーーーーーーーーーー

【イメージ】
・3つ添付させて頂きました。
・「デザイン2」のように立体的にお願いします。
・文字は横書きでお願いします。

ターゲット:40~50代・男性・会社員:年収1000万
参考LP:https://veltrano-k.jp/lp/seminar1/

【納品形式】
PNGファイル
記載項目
(メインタイトル)
黄金羅針盤アカデミー
実践攻略
前編
(サブタイトル)
相続市場を狙え!!
利回り20%&転売益2000万!
サイズ
• 要相談・教えてください。
希望イメージ
シンプル 複雑
単色 カラフル
暗い 明るい
日常 高級
遊び心 厳粛
未来的 伝統的
女性的 男性的
希望する色
赤系、青系、紫系
納品ファイル
• PNG形式 (.png)
■ 選んだ理由

カラー・フォント・配置がバランス良く感じました。

■ 提案者全員のお礼・コメント

この度は大変お世話になりました。
別案件でまた依頼したいと感じました。

```html
<!DOCTYPE html>
<html lang="ja">
<head>
<meta charset="utf-8">
<title>黄金羅針盤アカデミー 実践攻略 前編</title>
<link href="https://fonts.googleapis.com/css2?family=Noto+Serif+JP:wght@700;900&display=swap" rel="stylesheet">
<style>
  :root {
    --purple: #8d2180;
    --purple-soft: #a2489a;
    --ink: #2c0d28;
    --paper: #ffffff;
  }
  * { margin: 0; padding: 0; box-sizing: border-box; }
  html, body { width: 806px; height: 1200px; overflow: hidden; background: var(--paper); }
  .cover {
    position: relative; width: 806px; height: 1200px; overflow: hidden;
    font-family: "Noto Serif JP", serif; background: var(--paper);
  }
  .cover__head {
    position: absolute; left: 0; top: 0; width: 806px; height: 805px;
    background: var(--purple); color: var(--paper);
  }
  .title { font-weight: 900; line-height: 1; }
  .title__line { position: absolute; white-space: nowrap; letter-spacing: 4px; }
  .title__line--first { left: 170px; top: 62px; font-size: 138px; }
  .title__line--second { left: 170px; top: 210px; font-size: 138px; }
  .title__line--third { left: 150px; top: 370px; font-size: 112px; letter-spacing: 0; }
  .title__emblem {
    position: absolute; left: 520px; top: 80px; width: 96px; height: 96px;
    background: var(--purple-soft); border-radius: 6px;
  }
  .series {
    position: absolute; left: 161px; top: 533px; width: 511px; height: 147px;
    border: 7px solid var(--paper); display: flex; align-items: center; justify-content: center;
    font-size: 100px; font-weight: 900; letter-spacing: 6px; line-height: 1;
  }
  .volume {
    position: absolute; left: 161px; top: 704px; width: 511px; text-align: center;
    font-size: 40px; font-weight: 700; letter-spacing: 3px; line-height: 1.2;
  }
  .tagline {
    position: absolute; left: 100px; top: 860px; transform: rotate(-14deg);
    color: var(--purple); font-size: 38px; font-weight: 900; line-height: 1.2; text-align: center;
  }
  .promise { color: var(--ink); font-weight: 900; line-height: 1; }
  .promise__row { position: absolute; white-space: nowrap; }
  .promise__row--yield { left: 305px; top: 870px; font-size: 84px; }
  .promise__amp { position: absolute; left: 510px; top: 955px; font-size: 44px; color: var(--purple); }
  .promise__row--profit { left: 128px; top: 1005px; font-size: 92px; }
  .promise__num { color: var(--purple); }
  .author {
    position: absolute; left: 0; top: 1140px; width: 806px; text-align: center;
    color: var(--ink); font-size: 40px; font-weight: 700; letter-spacing: 3px; line-height: 1.2;
  }
  .author__suffix { font-size: 30px; }
</style>
</head>
<body>
<main class="cover">
  <section class="cover__head">
    <h1 class="title">
      <span class="title__line title__line--first">黄金</span>
      <span class="title__line title__line--second">羅針盤</span>
      <span class="title__line title__line--third">アカデミー</span>
    </h1>
    <div class="title__emblem" role="img" aria-label="タイトル横の小さなアイコン"></div>
    <div class="series">実践攻略</div>
    <p class="volume">-前編-</p>
  </section>

  <p class="tagline">相続市場<br>を狙え!!</p>

  <p class="promise">
    <span class="promise__row promise__row--yield">利回り<span class="promise__num">20%</span></span>
    <span class="promise__amp">&amp;</span>
    <span class="promise__row promise__row--profit">転売益<span class="promise__num">2000万</span>!</span>
  </p>

  <p class="author">ゴールドN <span class="author__suffix">著</span></p>
</main>
</body>
</html>
```